Bright Path Crest Home Realty yard sign Logo

UPDATE Design logo for Realty yard sign. 24x24 diamond or 36x24 Rectangle.
Open to all ideas. We are a discount firm but want to project a high end feel. We provide 100% of all services and extensive marketing for 1/2 the fee.
The following info must be on sign
BRIGHT PATH CREST (OR 1/3) HOME REALTY
Dennis Morrow 492-7306
CresthomeQV.com

Target Market(s)

home sellers and buyers

Industry/Entity Type

Real Estate yard sign please see sign attached in gif

Logo Text

Bright Path Crest Home Realty OR (1/3 IN PLACE OF CREST)

Requirements
Must have
• BRIGHT PATH CREST (OR 1/3) HOME REALTY Dennis Morrow 492-7306 CresthomeQV.com FOR SALE (optional)

```html
<!DOCTYPE html>
<html lang="en">
<head>
<meta charset="utf-8">
<title>Bright Path Crest Home Realty — Yard Sign</title>
<link href="https://fonts.googleapis.com/css2?family=Cinzel:wght@600;700&display=swap" rel="stylesheet">
<style>
  :root {
    --paper: #ffffff;
    --lime: #a6c12b;
    --azure: #0378d6;
  }
  html, body {
    margin: 0;
    padding: 0;
    width: 1200px;
    height: 1200px;
    overflow: hidden;
    background: var(--paper);
  }
  .yard-sign {
    display: block;
    width: 1200px;
    height: 1200px;
  }
  .sign-text {
    font-family: "Cinzel", "Trajan Pro", serif;
    font-weight: 700;
  }
  .band { fill: var(--azure); }
  .frame { fill: none; stroke: var(--lime); stroke-width: 28; }
  .for-sale { fill: var(--paper); font-size: 50px; }
  .brand { fill: var(--azure); }
  .brand-line-1 { font-size: 80px; }
  .brand-line-2 { font-size: 80px; }
  .brand-line-3 { font-size: 30px; }
  .brand-dot { fill: none; stroke: var(--lime); stroke-width: 12; }
  .agent { fill: var(--azure); font-size: 56px; }
  .website { fill: var(--azure); font-size: 34px; font-weight: 600; }
</style>
</head>
<body>
<svg class="yard-sign" viewBox="0 0 1932 1932" xmlns="http://www.w3.org/2000/svg">
  <defs>
    <clipPath id="sign-face">
      <polygon points="984,468 1443,927 984,1386 525,927"/>
    </clipPath>
  </defs>

  <g clip-path="url(#sign-face)">
    <rect class="band" x="400" y="622" width="1200" height="62"/>
    <rect class="band" x="400" y="1160" width="1200" height="300"/>
  </g>

  <polygon class="frame" points="984,454 1457,927 984,1400 511,927"/>

  <text class="sign-text for-sale" x="987" y="670" text-anchor="middle" textLength="244" lengthAdjust="spacingAndGlyphs">FOR SALE</text>

  <circle class="brand-dot" cx="767" cy="927" r="58"/>

  <text class="sign-text brand brand-line-1" x="702" y="848" textLength="568" lengthAdjust="spacingAndGlyphs">BRIGHT PATH</text>
  <text class="sign-text brand brand-line-2" x="878" y="930" textLength="380" lengthAdjust="spacingAndGlyphs">CREST HOME</text>
  <text class="sign-text brand brand-line-3" x="878" y="975" textLength="362" lengthAdjust="spacing">REALTY</text>

  <text class="sign-text agent" x="984" y="1053" text-anchor="middle" textLength="556" lengthAdjust="spacingAndGlyphs">DENNIS MORROW 492-7306</text>
  <text class="sign-text website" x="984" y="1106" text-anchor="middle" textLength="388" lengthAdjust="spacing">CRESTHOMEQV.COM</text>
</svg>
</body>
</html>
```